NEW YORK Plumbing/utility company 10 year anniversary business card

Looking For simple back and front business card would like to include a few things in description
We offer 24/7 emergency service
residential
commercial
industrial
municipal
services offered
Plumbing
hydro excavation
hydro jetting
Well pumps
Sewer pumps
water mains
sewer mains

```html
<!DOCTYPE html>
<html lang="en">
<head>
<meta charset="utf-8">
<title>Ridgeline Water &amp; Sewer – Business Cards</title>
<link rel="stylesheet" href="https://fonts.googleapis.com/css2?family=Montserrat:wght@600;700&family=Arimo:wght@400;700&display=swap">
<style>
  :root {
    --brand-blue: #0b4a8f;
    --brand-red: #e3161b;
    --paper: #f7f7f7;
    --stage: #d9d9d9;
    --ink-light: #ffffff;
  }
  * { box-sizing: border-box; margin: 0; padding: 0; }
  html, body { width: 1200px; height: 800px; overflow: hidden; }
  body {
    background: var(--stage);
    font-family: "Arimo", Arial, sans-serif;
    display: flex;
    flex-direction: column;
    align-items: center;
    justify-content: center;
    gap: 36px;
  }
  .card {
    position: relative;
    width: 640px;
    height: 366px;
    border-radius: 22px;
    overflow: hidden;
    box-shadow: 0 6px 16px rgba(0,0,0,0.18);
    border-bottom: 3px solid var(--brand-red);
  }
  .card-front { background: var(--paper); }
  .card-back { background: var(--brand-blue); }
  .front-bg { position: absolute; inset: 0; }

  .wordmark {
    position: absolute;
    font-family: "Montserrat", Arial, sans-serif;
    font-weight: 700;
    text-transform: uppercase;
    display: flex;
    align-items: center;
    gap: 12px;
  }
  .wordmark-dot { border-radius: 50%; flex: none; }
  .wordmark-text { line-height: 1.05; }

  .card-front .wordmark { left: 70px; top: 62px; color: var(--brand-blue); }
  .card-front .wordmark-dot { width: 38px; height: 38px; background: var(--brand-blue); }
  .card-front .wordmark-text { font-size: 34px; letter-spacing: 2px; }
  .card-front .wordmark-text small { display: block; font-size: 16px; letter-spacing: 4px; }

  .anniversary {
    position: absolute;
    left: 120px; top: 140px;
    font-family: "Montserrat", Arial, sans-serif;
    font-weight: 600;
    font-size: 13px;
    letter-spacing: 3px;
    text-transform: uppercase;
    color: var(--brand-red);
  }

  .holder {
    position: absolute;
    left: 150px; top: 268px;
    color: var(--ink-light);
  }
  .holder-name { font-size: 25px; font-weight: 700; }
  .holder-role { font-size: 13px; margin-top: 3px; }

  .contact {
    position: absolute;
    left: 372px; top: 232px;
    padding-left: 16px;
    border-left: 1px solid rgba(255,255,255,0.7);
    color: var(--ink-light);
    font-size: 13px;
    list-style: none;
    display: flex; flex-direction: column; gap: 7px;
  }
  .contact li { display: flex; align-items: center; gap: 8px; }
  .contact svg { width: 12px; height: 12px; fill: var(--ink-light); flex: none; }

  .card-back .wordmark {
    left: 0; right: 0; top: 60px;
    justify-content: center;
    color: var(--ink-light);
  }
  .card-back .wordmark-dot { width: 52px; height: 52px; background: var(--ink-light); }
  .card-back .wordmark-text { font-size: 44px; letter-spacing: 3px; }
  .card-back .wordmark-text small { display: block; font-size: 19px; letter-spacing: 5px; }

  .sectors {
    position: absolute;
    left: 0; right: 0; top: 160px;
    text-align: center;
    color: var(--ink-light);
    font-family: "Montserrat", Arial, sans-serif;
    font-weight: 600;
    font-size: 12px;
    letter-spacing: 3px;
    text-transform: uppercase;
  }

  .services {
    position: absolute;
    left: 0; right: 0; top: 210px;
    color: var(--ink-light);
    font-size: 17px;
    text-align: center;
    line-height: 1.5;
  }
  .service-row { display: flex; justify-content: center; gap: 10px; align-items: center; }
  .drop { width: 9px; height: 12px; fill: var(--ink-light); }

  .emergency {
    position: absolute;
    left: 0; right: 0; top: 292px;
    text-align: center;
  }
  .emergency span {
    display: inline-block;
    padding: 6px 18px;
    background: var(--brand-red);
    color: var(--ink-light);
    border-radius: 4px;
    font-family: "Montserrat", Arial, sans-serif;
    font-weight: 700;
    font-size: 14px;
    letter-spacing: 2px;
    text-transform: uppercase;
  }
</style>
</head>
<body>

  <section class="card card-front" aria-label="Business card front">
    <svg class="front-bg" viewBox="0 0 640 366" preserveAspectRatio="none" aria-hidden="true">
      <polygon points="0,300 640,112 640,366 0,366" fill="var(--brand-blue)"/>
      <line x1="0" y1="300" x2="640" y2="112" stroke="var(--brand-red)" stroke-width="7"/>
      <circle cx="14" cy="296" r="5" fill="var(--paper)" stroke="var(--brand-red)" stroke-width="3"/>
    </svg>

    <div class="wordmark">
      <span class="wordmark-dot"></span>
      <span class="wordmark-text">Ridgeline<small>Water &amp; Sewer</small></span>
    </div>

    <p class="anniversary">Celebrating 10 Years</p>

    <div class="holder">
      <p class="holder-name">Daniel Morrow</p>
      <p class="holder-role">Managing Director</p>
    </div>

    <ul class="contact">
      <li>
        <svg viewBox="0 0 24 24" aria-hidden="true"><path d="M6.6 10.8a15 15 0 0 0 6.6 6.6l2.2-2.2a1 1 0 0 1 1-.25 11 11 0 0 0 3.6.6 1 1 0 0 1 1 1V20a1 1 0 0 1-1 1A17 17 0 0 1 3 4a1 1 0 0 1 1-1h3.5a1 1 0 0 1 1 1 11 11 0 0 0 .6 3.6 1 1 0 0 1-.25 1z"/></svg>
        845-555-0182
      </li>
      <li>
        <svg viewBox="0 0 24 24" aria-hidden="true"><path d="M2 5h20v14H2zm2 2v.5l8 5 8-5V7l-8 5z"/></svg>
        info@ridgelinews.com
      </li>
      <li>
        <svg viewBox="0 0 24 24" aria-hidden="true"><circle cx="12" cy="12" r="10"/></svg>
        www.ridgelinews.com
      </li>
    </ul>
  </section>

  <section class="card card-back" aria-label="Business card back">
    <div class="wordmark">
      <span class="wordmark-dot"></span>
      <span class="wordmark-text">Ridgeline<small>Water &amp; Sewer</small></span>
    </div>

    <p class="sectors">Residential · Commercial · Industrial · Municipal</p>

    <div class="services">
      <p class="service-row">
        Plumbing
        <svg class="drop" viewBox="0 0 10 14" aria-hidden="true"><path d="M5 0C5 0 0 6.5 0 9.2A5 5 0 0 0 10 9.2C10 6.5 5 0 5 0z"/></svg>
        Hydro excavation
        <svg class="drop" viewBox="0 0 10 14" aria-hidden="true"><path d="M5 0C5 0 0 6.5 0 9.2A5 5 0 0 0 10 9.2C10 6.5 5 0 5 0z"/></svg>
        Hydro jetting
        <svg class="drop" viewBox="0 0 10 14" aria-hidden="true"><path d="M5 0C5 0 0 6.5 0 9.2A5 5 0 0 0 10 9.2C10 6.5 5 0 5 0z"/></svg>
        Well pumps
      </p>
      <p class="service-row">
        Sewer pumps
        <svg class="drop" viewBox="0 0 10 14" aria-hidden="true"><path d="M5 0C5 0 0 6.5 0 9.2A5 5 0 0 0 10 9.2C10 6.5 5 0 5 0z"/></svg>
        Water mains
        <svg class="drop" viewBox="0 0 10 14" aria-hidden="true"><path d="M5 0C5 0 0 6.5 0 9.2A5 5 0 0 0 10 9.2C10 6.5 5 0 5 0z"/></svg>
        Sewer mains
      </p>
    </div>

    <p class="emergency"><span>24/7 Emergency Service</span></p>
  </section>

</body>
</html>
```